Whitening Flyer

I need an informational flyer for my dental practice. The flyer will describe the whitening services that are available at my practice and show price of each whitening service. We currently gave a 3 fold brochure, but I prefer something with a more professional look, and personalized with our branding and practice colors. I have attached the current flyer for you to use similar text. I will also attach a flyer that I have used in the past that could demonstrate my branding or feel free to view my website: www.pemtrix.com

```html
<!DOCTYPE html>
<html lang="en">
<head>
<meta charset="utf-8">
<title>Brightline Dental – Whitening Flyer</title>
<link rel="stylesheet" href="https://fonts.googleapis.com/css2?family=Montserrat:wght@400;600&family=Roboto:wght@300;400;500;700&display=swap">
<style>
  :root{
    --crimson:#d0143f;
    --charcoal:#333333;
    --gold:#f1c35a;
    --white:#ffffff;
    --ink:#2b2b2b;
    --quote-grey:#bdbdbd;
  }
  *{margin:0;padding:0;box-sizing:border-box;}
  html,body{width:958px;height:1200px;overflow:hidden;background:var(--white);}
  body{font-family:"Roboto",sans-serif;color:var(--ink);}
  .flyer{position:relative;width:958px;height:1200px;overflow:hidden;background:var(--white);}
  .backdrop{position:absolute;inset:0;}

  .brand{position:absolute;left:44px;top:58px;width:340px;text-align:center;}
  .brand-name{font-family:"Roboto",sans-serif;font-weight:700;font-size:40px;color:var(--crimson);letter-spacing:.5px;display:flex;align-items:center;justify-content:center;gap:12px;}
  .brand-dot{width:16px;height:16px;border-radius:50%;background:var(--crimson);}

  .tagline{position:absolute;left:452px;top:138px;font-size:30px;font-weight:300;line-height:1.18;color:var(--crimson);}
  .tagline strong{font-weight:700;}

  .intro{position:absolute;left:44px;top:262px;width:310px;font-size:13.6px;font-weight:300;line-height:1.72;color:var(--crimson);text-align:justify;}

  .packages-title{position:absolute;left:44px;top:514px;font-family:"Montserrat",sans-serif;color:var(--white);font-size:23px;line-height:1.16;}
  .packages-title span{display:block;font-weight:400;}
  .packages-title strong{display:block;font-weight:600;}

  .package{position:absolute;left:30px;width:420px;}
  .package-bar{position:absolute;left:50px;top:16px;width:250px;height:38px;background:var(--gold);padding-left:24px;display:flex;align-items:center;font-size:15.5px;font-weight:500;color:var(--ink);}
  .package-price{position:absolute;left:0;top:0;width:70px;height:70px;border-radius:50%;background:var(--gold);display:flex;align-items:center;justify-content:center;font-size:23px;font-weight:500;color:var(--ink);z-index:1;}
  .package-desc{position:absolute;left:78px;top:66px;width:230px;font-size:9px;font-weight:300;line-height:1.3;color:var(--white);text-align:justify;}

  .testimonial{position:absolute;left:475px;top:770px;width:220px;height:220px;display:flex;flex-direction:column;align-items:center;justify-content:center;text-align:center;}
  .testimonial-mark{font-family:"Roboto",sans-serif;font-weight:700;font-size:96px;line-height:.7;height:50px;color:var(--quote-grey);}
  .testimonial-text{margin-top:24px;font-size:12px;line-height:1.3;color:var(--white);width:162px;}

  .contact-social{position:absolute;left:44px;top:1122px;display:grid;grid-template-columns:150px 130px;row-gap:14px;font-size:10.5px;color:var(--ink);}
  .contact-item{display:flex;align-items:center;gap:7px;white-space:nowrap;}
  .contact-dot{width:14px;height:14px;border-radius:50%;background:var(--ink);flex:none;}
  .contact-item svg{flex:none;}

  .phone{position:absolute;left:530px;top:1110px;display:flex;align-items:center;gap:10px;font-size:30px;font-weight:700;color:var(--charcoal);}
  .address{position:absolute;left:494px;top:1158px;display:flex;align-items:center;gap:6px;font-size:17px;color:var(--charcoal);}
</style>
</head>
<body>
<main class="flyer">
  <svg class="backdrop" width="958" height="1200" viewBox="0 0 958 1200">
    <path class="dark-band" fill="#333333"
      d="M0,470 C100,428 220,488 320,478 C410,470 420,410 470,398 L958,398 L958,1110 C780,1080 600,1082 450,1108 C300,1090 150,1088 0,1132 Z"/>
    <path class="portrait-photo" role="img" aria-label="Photo of a smiling senior woman with short grey hair"
      fill="url(#portraitTones)"
      d="M958,240 C880,258 800,292 720,284 C620,274 458,270 452,390 C450,470 520,540 552,600 C568,680 574,760 588,830 L958,830 Z"/>
    <path class="portrait-edge" fill="none" stroke="#d0143f" stroke-width="6"
      d="M958,240 C880,258 800,292 720,284 C620,274 458,270 452,390 C450,470 520,540 552,600 C568,680 574,760 588,830"/>
    <circle class="couple-photo" role="img" aria-label="Photo of a smiling young couple" cx="820" cy="790" r="112"
      fill="url(#coupleTones)" stroke="#ffffff" stroke-width="5"/>
    <circle class="testimonial-disc" cx="585" cy="880" r="118" fill="#333333" stroke="#ffffff" stroke-width="4"/>
    <path class="footer-band" fill="#ffffff"
      d="M0,1132 C150,1088 300,1090 450,1108 C600,1082 780,1080 958,1110 L958,1200 L0,1200 Z"/>
    <path class="footer-divider" fill="none" stroke="#333333" stroke-width="2.5"
      d="M448,1108 C438,1140 445,1175 462,1200"/>
    <defs>
      <linearGradient id="portraitTones" x1="0" y1="0" x2="1" y2="1">
        <stop offset="0" stop-color="#d9d2c8"/>
        <stop offset=".45" stop-color="#a8704e"/>
        <stop offset="1" stop-color="#e8e4de"/>
      </linearGradient>
      <linearGradient id="coupleTones" x1="0" y1="0" x2="1" y2="1">
        <stop offset="0" stop-color="#5a3a2a"/>
        <stop offset=".6" stop-color="#8a5a40"/>
        <stop offset="1" stop-color="#e6e2dc"/>
      </linearGradient>
    </defs>
  </svg>

  <header class="brand">
    <div class="brand-name"><span class="brand-dot"></span>Brightline Dental</div>
  </header>

  <p class="tagline">“At <strong>Brightline Dental</strong>,<br>we care about your smile”</p>

  <p class="intro">Our office staff has been trained extensively to assist you step by step in the whitening process. From pre-op to post op, they are by your side to help with questions or concerns Our office offers multiple options fitting every budget. You can also speak with our office manager about possible payment options. Some restrictions may apply and results vary.</p>

  <h2 class="packages-title"><span>WHICH</span><strong>WHITENING IS RIGHT?</strong></h2>

  <section class="package" style="top:585px">
    <div class="package-price">$10</div>
    <div class="package-bar">Basic Whitening Package</div>
    <p class="package-desc">One Upper and Lower one-time use tray set and care instructions. No appointment needed</p>
  </section>

  <section class="package" style="top:672px">
    <div class="package-price">$80</div>
    <div class="package-bar">Silver Whitening Package</div>
    <p class="package-desc">Ten Upper and Lower one-time use trays and care instructions. No appointment needed</p>
  </section>

  <section class="package" style="top:758px">
    <div class="package-price">$275</div>
    <div class="package-bar">Golden Whitening Package</div>
    <p class="package-desc">Custom made upper and lower whitening trays to be used at home. One 30 min office appointment for impressions. 4 tubes of professional whitening agent. At home care instructions (refills available for purchase of $35)</p>
  </section>

  <section class="package" style="top:860px">
    <div class="package-price">$375</div>
    <div class="package-bar">Diamond Whitening Package</div>
    <p class="package-desc">One 90 min office appointment for chairside professional-grade whitening. At home care instructions.</p>
  </section>

  <section class="package" style="top:944px">
    <div class="package-price">$475</div>
    <div class="package-bar">Platinum Whitening Package</div>
    <p class="package-desc">One 2hr office appointment for chairside professional-grade whitening. At home care instructions.</p>
  </section>

  <blockquote class="testimonial">
    <div class="testimonial-mark">“</div>
    <p class="testimonial-text">I Just Love Dr. Harlow she and staff are so amazing! Hygienist was thorough and friendly. I would definitely recommend to everyone! I can’t wait for my next visit!</p>
  </blockquote>

  <footer>
    <div class="contact-social">
      <span class="contact-item"><span class="contact-dot"></span>brightline_dental_studio</span>
      <span class="contact-item"><span class="contact-dot"></span>Brightline Dental</span>
      <span class="contact-item">
        <svg width="14" height="11" viewBox="0 0 14 11"><rect x=".75" y=".75" width="12.5" height="9.5" fill="none" stroke="#2b2b2b" stroke-width="1.5"/><path d="M1 1 L7 6 L13 1" fill="none" stroke="#2b2b2b" stroke-width="1.5"/></svg>
        hello@pemtrix.com</span>
      <span class="contact-item">
        <svg width="14" height="14" viewBox="0 0 14 14" fill="none" stroke="#2b2b2b" stroke-width="1.2"><circle cx="7" cy="7" r="6"/><ellipse cx="7" cy="7" rx="2.6" ry="6"/><path d="M1 7h12M2 4h10M2 10h10"/></svg>
        www.pemtrix.com</span>
    </div>

    <div class="phone">
      <svg width="24" height="26" viewBox="0 0 24 24"><path fill="#333333" d="M6.6 10.8a15.1 15.1 0 0 0 6.6 6.6l2.2-2.2a1 1 0 0 1 1-.25 11.4 11.4 0 0 0 3.6.57 1 1 0 0 1 1 1V20a1 1 0 0 1-1 1A17 17 0 0 1 3 4a1 1 0 0 1 1-1h3.5a1 1 0 0 1 1 1c0 1.25.2 2.45.57 3.57a1 1 0 0 1-.25 1z"/></svg>
      (555)014-2290
    </div>
    <div class="address">
      <svg width="11" height="16" viewBox="0 0 12 18"><path fill="#333333" d="M6 0a6 6 0 0 0-6 6c0 4.5 6 12 6 12s6-7.5 6-12a6 6 0 0 0-6-6zm0 8.5A2.5 2.5 0 1 1 6 3.5a2.5 2.5 0 0 1 0 5z"/></svg>
      1420 Magnolia Ave, Riverton, LA, 70000
    </div>
  </footer>
</main>
</body>
</html>
```